Exciting Poster Project: 4 posters for Employee Benefit Program

We are an entrepreneurial healthcare IT company that is creating an internal campaign to launch our 2017 Culture and Professional Development goals for our internal staff.

We need 4 posters utilizing the 4 campaign logos (attached) that are tied together visually into a cohesive campaign.

A PPT is included that shows the other wall art that currently exists on the walls. The new posters will share a space with these pieces.

The posters may be mounted side by side, or stand alone on a wall- so the design should work both ways. Each poster should include its own icon and the tag line provided along with topics provided that fall under this category. The posters size can be dictated by your design, but the text should be legible from a minimum of 8 feet away.

At the bottom of each poster should include all 4 icons in order to tie the entire campaign together (perhaps they can be arranged together like a diamond shape with the primary one as the biggest diamond)

Our company website for our external branding is: www.pelmaroq.com
We have included our branding guidelines for our external brand, and ppts and graphics for our internal brand.

1) Poster 1:
a. Header: Better Today Than Yesterday
b. Sub-title: Personal and Professional Growth
c. Description: We are committed to helping you build on your strengths and passions and support you your career advancement goals. We have a variety of training and development programs available to help you reach your top potential!
Leadership Development Programs
1. Supervisor Training
2. Women’s Leadership
3. Leadership Meet-Ups
4. MBA Program
Staff Development
1. Continuing Education Fund
2. Book Club
3. Pelmaroq University
4. Mentorship
5. Learning Libraries
6. Department Wide Training Events

2) Poster 2:
a. Header: Perform at Highest Capacity
b. Sub-title: Be Your Best Self
c. Description: We are committed to providing programs that bring focus to your health and overall personal wellness to encourage a well balanced life
i. Healthy Living
1. Health and wellness seminars
2. Nutrition: Fruit Delivery
ii. Fitness:
1. Step Challenge
2. Virtual 5k
3. Recess
4. Golf Lessons
5. Ping Pong Club
iii. Creativity:
1. Painting
2. Photography Club
3. Virtual Trivia
iv. Mental Health:
1. Massage Therapy
2. EAP Education
v. Financial
1. 401(k)
2. Retirement education/financial planning seminars
3. Global Insurance Program education

3) Poster 3:
a. Header: Passionate Urgent and Driven to Success
b. Sub-Header: Innovation and Strategy
c. Description: We are committed to helping you connect the dots both in the industry and with our internal goals , mission, and vision.
i. Quarterly All-Hands
ii. Lumiverse
1. Internally: Departmental and Product Updates
2. Externally: Industry Knowledge
3. Culturally: Peer to Peer Community

4) Poster 4:
a. Header: Succeed as a Team
b. Sub-Header: Cultivating Collaboration
c. Description: We are committed to creating a culture of appreciation, teamwork, and supporting an open communication. All feedback and ideas are welcome here!
i. Team Building Events
1. Employee Focused
a. Summer Picnic
b. Employee Appreciation
c. Diwali
d. Holiday Party
e. Department Appreciation
2. Family Friendly
a. Halloween
b. Bring your Kids to Work Day
3. Awards
a. Peer to Peer: QuickNod Awards
b. Leadership: Crest of Merit
4. Surveys
a. New Hire
b. Employee Engagement
Updates

Target Market(s)

Internal Employees

Industry/Entity Type

Healthcare

Font styles to use
Sans Serif

Requirements
Must have
• Job Type: Posters
• Task Outline: Create Vector Art for 4 icons and 4 posters
• Fonts and Styles to Use: SourceSansPro
Nice to have
• There is an attachment with suggested concepts and styles that we like.
Should not have
• The poster should not be very wordy or hard to read in passing.

```html
<!DOCTYPE html>
<html lang="en">
<head>
<meta charset="utf-8">
<title>Pelmaroq Culture Campaign Posters</title>
<link rel="stylesheet" href="https://fonts.googleapis.com/css2?family=Oswald:wght@300;400;600;700&family=Source+Sans+3:wght@400;600;700;800&display=swap">
<style>
:root{
  --navy:#2c3868;
  --navy-dark:#232d57;
  --orange:#ee5a27;
  --orange-light:#f47a3c;
  --ink:#2c3868;
  --text:#3a3f55;
  --paper:#ffffff;
  --backdrop:#ffffff;
  --rule:#e3e5ee;
}
*{box-sizing:border-box;margin:0;padding:0}
html,body{width:912px;height:1200px;overflow:hidden;background:var(--backdrop)}
body{font-family:"Source Sans 3",Arial,sans-serif;color:var(--text)}
.campaign{display:grid;grid-template-columns:440px 440px;grid-template-rows:584px 584px;gap:16px;padding:8px}
.poster{background:var(--paper);display:flex;flex-direction:column;box-shadow:0 0 0 1px var(--rule)}
.hero{height:200px;position:relative;overflow:hidden;display:flex;align-items:center;padding:0 22px}
.hero--navy{background:var(--navy)}
.hero--orange{background:linear-gradient(135deg,var(--orange-light),var(--orange))}
.hero-art{position:absolute;right:18px;top:28px;width:160px;height:144px;border-radius:6px}
.hero--navy .hero-art{background:radial-gradient(circle at 60% 40%,rgba(255,255,255,.28),rgba(255,255,255,.06))}
.hero--orange .hero-art{background:radial-gradient(circle at 60% 40%,rgba(255,255,255,.32),rgba(44,56,104,.18))}
.headline{font-family:Oswald,Arial,sans-serif;text-transform:uppercase;color:#fff;position:relative;z-index:1;line-height:.95}
.headline .big{display:block;font-weight:700;font-size:58px;letter-spacing:.5px}
.headline .light{display:block;font-weight:300;font-size:24px;letter-spacing:.5px;margin-top:4px}
.headline .thin{display:block;font-weight:300;font-size:34px}
.headline .navy{color:var(--navy)}
.headline .accent{color:var(--orange)}
.headline .huge{display:block;font-weight:700;font-size:80px}
.body{flex:1;padding:16px 24px 0}
.section-title{display:flex;align-items:center;gap:10px;font-weight:800;font-size:20px;color:var(--ink);margin-bottom:6px}
.section-title .dot{width:24px;height:24px;border-radius:50%;background:var(--orange);flex:none}
.intro{font-size:12.5px;line-height:1.35;margin-bottom:12px}
.cols{display:grid;grid-template-columns:1fr 1fr;gap:14px}
.tag{background:var(--orange);color:#fff;font-weight:800;font-size:12px;text-transform:uppercase;padding:5px 8px;line-height:1.15}
.list{list-style:none;font-size:12.5px;line-height:1.45;padding:6px 8px}
.list li::before{content:"• ";color:var(--navy)}
.group{font-size:12px;line-height:1.3;list-style:none}
.group>li{margin-bottom:4px}
.group .cat{font-weight:800;text-transform:uppercase;color:var(--ink)}
.group .cat::before{content:"• "}
.group .sub{padding-left:10px;display:block}
.pillars{display:grid;grid-template-columns:repeat(3,1fr);margin-top:10px;border:1px solid var(--rule)}
.pillar{text-align:center;padding:10px 6px;border-right:1px solid var(--rule);font-size:11.5px;line-height:1.25}
.pillar:last-child{border-right:0}
.pillar .ico{width:30px;height:30px;margin:0 auto 6px}
.pillar b{display:block;color:var(--orange);font-weight:800;text-transform:uppercase;font-size:11px}
.footer{padding:8px 20px 14px;text-align:center}
.brand{display:inline-flex;align-items:center;gap:8px;font-weight:800;font-size:26px;color:var(--navy);margin-bottom:12px}
.brand .mark{width:16px;height:16px;background:var(--orange)}
.family{display:flex;justify-content:space-between}
.family span{display:flex;align-items:center;gap:5px;font-size:8.5px;line-height:1.1;color:var(--ink);text-align:left;width:24%}
.family i{width:16px;height:16px;border-radius:50%;background:var(--navy);flex:none}
.family .on i{background:var(--orange)}
</style>
</head>
<body>
<main class="campaign">

  <article class="poster">
    <header class="hero hero--navy">
      <h1 class="headline"><span class="big">Better<br>Today</span><span class="light">Than Yesterday</span></h1>
      <div class="hero-art" role="img" aria-label="Illustration of a person beside a glowing light bulb idea"></div>
    </header>
    <section class="body">
      <h2 class="section-title"><span class="dot"></span>Personal and Professional Growth</h2>
      <p class="intro">We are committed to helping you build on your strengths and passions and support you your career advancement goals. We have a variety of training and development programs available to help you reach your top potential!</p>
      <div class="cols">
        <div><div class="tag">Leadership Development Programs</div>
          <ul class="list"><li>Supervisor Training</li><li>Women’s Leadership</li><li>Leadership Meet-Ups</li><li>MBA Program</li></ul></div>
        <div><div class="tag">Staff Development</div>
          <ul class="list"><li>Continuing Education Fund</li><li>Book Club</li><li>Pelmaroq University</li><li>Mentorship</li><li>Learning Libraries</li><li>Department Wide Training Events</li></ul></div>
      </div>
    </section>
    <footer class="footer">
      <div class="brand"><span class="mark"></span>Pelmaroq</div>
      <div class="family"><span class="on"><i></i>Personal and Professional Growth</span><span><i></i>Be Your Best Self</span><span><i></i>Innovation and Strategy</span><span><i></i>Cultivating Collaboration</span></div>
    </footer>
  </article>

  <article class="poster">
    <header class="hero hero--orange">
      <h1 class="headline"><span class="thin">Perform at</span><span class="big navy">Highest<br>Capacity</span></h1>
      <div class="hero-art" role="img" aria-label="Illustration of a person with a rating of stars and a check mark"></div>
    </header>
    <section class="body">
      <h2 class="section-title"><span class="dot"></span>Be Your Best Self</h2>
      <p class="intro">We are committed to providing programs that bring focus to your health and overall personal wellness to encourage a well balanced life</p>
      <div class="cols">
        <ul class="group">
          <li><span class="cat">Healthy Living</span><span class="sub">– Health and wellness seminars</span></li>
          <li><span class="cat">Nutrition</span><span class="sub">– Fruit Delivery</span></li>
          <li><span class="cat">Fitness</span><span class="sub">– Step Challenge<br>– Virtual 5k<br>– Recess<br>– Golf Lessons<br>– Ping Pong Club</span></li>
          <li><span class="cat">Creativity</span><span class="sub">– Painting<br>– Photography Club<br>– Virtual Trivia</span></li>
        </ul>
        <ul class="group">
          <li><span class="cat">Mental Health</span><span class="sub">– Massage Therapy<br>– EAP Education</span></li>
          <li><span class="cat">Financial</span><span class="sub">– 401(k)<br>– Retirement education/ financial planning seminars<br>– Global Insurance Program education</span></li>
        </ul>
      </div>
    </section>
    <footer class="footer">
      <div class="brand"><span class="mark"></span>Pelmaroq</div>
      <div class="family"><span><i></i>Personal and Professional Growth</span><span class="on"><i></i>Be Your Best Self</span><span><i></i>Innovation and Strategy</span><span><i></i>Cultivating Collaboration</span></div>
    </footer>
  </article>

  <article class="poster">
    <header class="hero hero--orange">
      <h1 class="headline"><span class="thin">Succeed as a</span><span class="huge navy">Team</span></h1>
      <div class="hero-art" role="img" aria-label="Illustration of a group of three colleagues with a speech bubble"></div>
    </header>
    <section class="body">
      <h2 class="section-title"><span class="dot"></span>Cultivating Collaboration</h2>
      <p class="intro">We are committed to creating a culture of appreciation, teamwork, and supporting an open communication. All feedback and ideas are welcome here!</p>
      <div class="cols">
        <ul class="group">
          <li><span class="cat">Team Building Events</span><span class="sub">– Employee Focused<br>– Summer Picnic<br>– Employee Appreciation<br>– Diwali<br>– Holiday Party<br>– Department Appreciation</span></li>
          <li><span class="cat">Family Friendly</span><span class="sub">– Halloween<br>– Bring your Kids to Work Day</span></li>
        </ul>
        <ul class="group">
          <li><span class="cat">Awards</span><span class="sub">– Peer to Peer: QuickNod Awards<br>– Leadership: Crest of Merit</span></li>
          <li><span class="cat">Surveys</span><span class="sub">– New Hire<br>– Employee Engagement</span></li>
        </ul>
      </div>
    </section>
    <footer class="footer">
      <div class="brand"><span class="mark"></span>Pelmaroq</div>
      <div class="family"><span><i></i>Personal and Professional Growth</span><span><i></i>Be Your Best Self</span><span><i></i>Innovation and Strategy</span><span class="on"><i></i>Cultivating Collaboration</span></div>
    </footer>
  </article>

  <article class="poster">
    <header class="hero hero--navy">
      <h1 class="headline"><span class="light">Passionate<br>Urgent and</span><span class="big" style="font-size:44px">Driven to</span><span class="big accent" style="font-size:50px">Success</span></h1>
      <div class="hero-art" role="img" aria-label="Illustration of a team with a rising arrow and a trophy"></div>
    </header>
    <section class="body">
      <h2 class="section-title"><span class="dot"></span>Innovation and Strategy</h2>
      <p class="intro">We are committed to helping you connect the dots both in the industry and with our internal goals , mission, and vision.</p>
      <ul class="group">
        <li><span class="cat">Quarterly All-Hands</span></li>
        <li><span class="cat">Lumiverse</span></li>
      </ul>
      <div class="pillars">
        <div class="pillar">
          <svg class="ico" viewBox="0 0 30 30"><rect x="3" y="7" width="20" height="20" fill="none" stroke="#2c3868" stroke-width="3"/><path d="M12 18 L27 3 M18 3 H27 V12" fill="none" stroke="#2c3868" stroke-width="3"/></svg>
          <b>Externally</b>Industry Knowledge</div>
        <div class="pillar">
          <svg class="ico" viewBox="0 0 30 30"><rect x="3" y="3" width="20" height="20" fill="none" stroke="#2c3868" stroke-width="3"/><path d="M27 27 L12 12 M12 21 V12 H21" fill="none" stroke="#2c3868" stroke-width="3"/></svg>
          <b>Internally</b>Departmental and Product Updates</div>
        <div class="pillar">
          <svg class="ico" viewBox="0 0 30 30"><circle cx="8" cy="10" r="4" fill="#2c3868"/><circle cx="22" cy="10" r="4" fill="#2c3868"/><circle cx="15" cy="13" r="4.5" fill="#2c3868"/><rect x="2" y="16" width="12" height="9" rx="4" fill="#2c3868"/><rect x="16" y="16" width="12" height="9" rx="4" fill="#2c3868"/><rect x="8" y="19" width="14" height="9" rx="4" fill="#2c3868"/></svg>
          <b>Culturally</b>Peer to Peer Community</div>
      </div>
    </section>
    <footer class="footer">
      <div class="brand"><span class="mark"></span>Pelmaroq</div>
      <div class="family"><span><i></i>Personal and Professional Growth</span><span><i></i>Be Your Best Self</span><span class="on"><i></i>Innovation and Strategy</span><span><i></i>Cultivating Collaboration</span></div>
    </footer>
  </article>

</main>
</body>
</html>
```